Business Card Design

Im a small business that specialises in all aspects of sign installation, big and small, domestic and commercial. I have a construction and carpentry background. I'm after a professional looking business card, that has my logo as the forefront of the card incorporating the same colours as the my logo. No slogan as yet, but open to suggestions. The final design should communicate quality and class workmanship.

Target Market(s)

Managers and Owners of businesses

Industry/Entity Type

Small Business

Contact Information for Business Card

Carwyn Solbeck
Mob: 0417295036
Email: kto.fitouts@quillmail.net

Sign Installation
Property Improvement and Maintenance
Trade Services

Colors
dbdbdb
000000
ffffff

Requirements
Must have
• Logo
My name
My contact details
What I specialise in
Nice to have
• background image/images that are only just noticeable and do not take away from the logo or text.
Should not have
• No colours that contrast from my logo
No heavy machinery images to be used
Logo must stand out

```html
<!DOCTYPE html>
<html lang="en">
<head>
<meta charset="utf-8">
<title>KTO Installations – Business Card</title>
<link href="https://fonts.googleapis.com/css2?family=Bebas+Neue&display=swap" rel="stylesheet">
<style>
  :root {
    --bg-glow: #3b4144;
    --bg-mid: #1b1e20;
    --bg-edge: #0d0e0f;
    --brand-blue: #2452e8;
    --text-light: #dbdbdb;
    --panel-fill: rgba(3, 3, 3, 0.88);
    --panel-border: #cfcfcf;
  }
  html, body {
    margin: 0;
    padding: 0;
    width: 1200px;
    height: 741px;
    overflow: hidden;
    background: var(--bg-edge);
  }
  .card {
    position: relative;
    width: 1200px;
    height: 741px;
    background: radial-gradient(ellipse 520px 360px at 600px 250px, var(--bg-glow) 0%, var(--bg-mid) 55%, var(--bg-edge) 100%);
    font-family: "Bebas Neue", "Oswald", sans-serif;
    color: var(--text-light);
  }
  .brand {
    position: absolute;
    top: 155px;
    left: 0;
    width: 1200px;
    display: flex;
    justify-content: center;
    align-items: center;
    gap: 22px;
  }
  .brand-mark {
    width: 118px;
    height: 118px;
  }
  .brand-name {
    font-size: 84px;
    line-height: 1;
    letter-spacing: 3px;
    color: var(--brand-blue);
    padding-top: 8px;
  }
  .contact-panel {
    position: absolute;
    left: 143px;
    top: 343px;
    width: 912px;
    height: 255px;
    box-sizing: border-box;
    border: 1.5px solid var(--panel-border);
    border-radius: 9px;
    background: var(--panel-fill);
    text-align: center;
  }
  .contact-panel p {
    margin: 0;
    position: absolute;
    left: 0;
    width: 100%;
    line-height: 1;
    text-shadow: 2px 3px 3px rgba(0, 0, 0, 0.9), 0 0 1px #fff;
  }
  .person-name {
    top: 22px;
    font-size: 50px;
    letter-spacing: 4px;
  }
  .phone {
    top: 116px;
    font-size: 37px;
    letter-spacing: 5px;
  }
  .email {
    top: 152px;
    font-size: 27px;
    letter-spacing: 3px;
  }
  .services {
    top: 206px;
    font-size: 21px;
    letter-spacing: 3px;
  }
</style>
</head>
<body>
  <main class="card">
    <header class="brand">
      <svg class="brand-mark" viewBox="0 0 118 118" aria-hidden="true">
        <circle cx="59" cy="59" r="52" fill="none" stroke="var(--brand-blue)" stroke-width="9"/>
      </svg>
      <span class="brand-name">KTO Installations</span>
    </header>
    <section class="contact-panel">
      <p class="person-name">Carwyn Solbeck</p>
      <p class="phone">Mob: 0417295036</p>
      <p class="email">Email: kto.fitouts@quillmail.net</p>
      <p class="services">Sign Installation Property Improvement and Maintenance Trade Services</p>
    </section>
  </main>
</body>
</html>
```